Business Card front and back

I am looking for business card design. I really really like the design file I uploaded named 627788_19250069_3478263_85f427ee_image

Target Market(s)

Corporate Fitness High end Private country club

Industry/Entity Type

Fitness Industry

Contact Information for Business Card

The last image I like as an example I uploaded a bunch of my logos. The file labeled "the signature" is my business card information for you to use

Colors
0054AA
0677BA
7BADD7
CADEEF
E8F1F8

Requirements
Must have
• E-mail sigThe file I uploaded labeled "627788_19250069_3478263_85f427ee_image" with all the plus signs on the back if those could be the logo symbol I uploaded labeled "1 back.png"

```html
<!DOCTYPE html>
<html lang="en">
<head>
<meta charset="utf-8">
<title>Summit Form Wellness – Business Card</title>
<link rel="stylesheet" href="https://fonts.googleapis.com/css2?family=Lato:wght@400;700;900&display=swap">
<style>
  :root {
    --backdrop: #1c1c1e;
    --card: #333335;
    --blue: #4a80c8;
    --white: #ffffff;
    --silver: #b9b9bc;
    --muted: #e6e6e6;
  }
  * { box-sizing: border-box; margin: 0; padding: 0; }
  html, body {
    width: 1200px; height: 1122px; overflow: hidden;
    background: var(--backdrop);
    font-family: "Lato", sans-serif;
  }
  .sheet {
    position: relative; width: 1200px; height: 1122px;
    display: flex; flex-direction: column; align-items: center; justify-content: center; gap: 34px;
  }
  .card {
    position: relative; width: 900px; height: 514px;
    background: var(--card); border-radius: 30px; overflow: hidden;
  }
  .brand { display: flex; align-items: center; gap: 22px; white-space: nowrap; }
  .brand__mark { width: 54px; height: 54px; background: currentColor; border-radius: 6px; flex: none; }
  .brand__name {
    font-weight: 900; text-transform: uppercase; letter-spacing: 0.06em; line-height: 1.05;
  }
  .brand__line { display: block; }

  /* Back side */
  .card--back { display: flex; align-items: center; justify-content: center; }
  .card--back .brand { color: var(--silver); }
  .card--back .brand__name { font-size: 52px; }

  /* Front side */
  .contact { position: absolute; left: 64px; top: 96px; white-space: nowrap; }
  .contact__name {
    color: var(--blue); font-weight: 700; font-size: 46px; text-transform: uppercase; letter-spacing: 0.01em; line-height: 1;
  }
  .contact__role { color: var(--white); font-size: 26px; margin-top: 6px; letter-spacing: 0.03em; }
  .divider {
    position: absolute; left: 64px; top: 200px; width: 740px; height: 2px; background: var(--blue);
  }
  .contact__list { position: absolute; left: 64px; top: 226px; list-style: none; }
  .contact__item {
    display: flex; align-items: center; gap: 16px; color: var(--muted); font-size: 22px; letter-spacing: 0.04em; margin-bottom: 12px; white-space: nowrap;
  }
  .contact__item svg { width: 22px; height: 22px; fill: var(--blue); flex: none; }
  .card--front .brand { position: absolute; right: 70px; top: 98px; color: var(--white); gap: 16px; }
  .card--front .brand__name { font-size: 34px; }
  .card--front .brand__mark { width: 38px; height: 38px; background: var(--blue); }
  .regions {
    position: absolute; right: 70px; bottom: 106px;
    color: var(--white); font-size: 22px; letter-spacing: 0.08em; white-space: nowrap;
  }
  .footer-band { position: absolute; left: 0; bottom: 0; width: 100%; height: 70px; }
  .footer-band svg { display: block; width: 100%; height: 100%; }
  .website {
    position: absolute; right: 60px; bottom: 20px;
    color: var(--white); font-size: 24px; letter-spacing: 0.1em; text-transform: uppercase; white-space: nowrap;
  }
</style>
</head>
<body>
<main class="sheet">
  <section class="card card--back" aria-label="Card back">
    <div class="brand">
      <span class="brand__mark"></span>
      <span class="brand__name">Summit Form Wellness</span>
    </div>
  </section>

  <section class="card card--front" aria-label="Card front">
    <div class="contact">
      <h1 class="contact__name">Dana Morrow</h1>
      <p class="contact__role">Consultant</p>
    </div>

    <div class="brand">
      <span class="brand__name">
        <span class="brand__line">Summit Form</span>
        <span class="brand__line">Wellness</span>
      </span>
      <span class="brand__mark"></span>
    </div>

    <div class="divider"></div>

    <ul class="contact__list">
      <li class="contact__item">
        <svg viewBox="0 0 24 24" aria-hidden="true"><path d="M6.6 10.8a15.1 15.1 0 0 0 6.6 6.6l2.2-2.2c.3-.3.7-.4 1-.2 1.1.4 2.3.6 3.6.6.6 0 1 .4 1 1V20c0 .6-.4 1-1 1A17 17 0 0 1 3 4c0-.6.4-1 1-1h3.5c.6 0 1 .4 1 1 0 1.3.2 2.5.6 3.6.1.3 0 .7-.2 1z"/></svg>
        <span>555-014-2870</span>
      </li>
      <li class="contact__item">
        <svg viewBox="0 0 24 24" aria-hidden="true"><path d="M2 5h20v14H2V5zm2 2v.5l8 5 8-5V7H4zm0 2.9V17h16V9.9l-8 5-8-5z"/></svg>
        <span>dana@summitformwellness.co</span>
      </li>
    </ul>

    <p class="regions">ND. SD. MN. NE. IA. KS</p>

    <div class="footer-band">
      <svg viewBox="0 0 900 70" preserveAspectRatio="none" aria-hidden="true">
        <polygon points="0,22 380,70 0,70" fill="var(--white)"/>
        <polygon points="345,70 420,0 900,0 900,70" fill="var(--blue)"/>
      </svg>
    </div>
    <p class="website">www.summitformwellness.co</p>
  </section>
</main>
</body>
</html>
```